CloudRiver Business Card

I need something that flows with the logo and looks professional but creative. I included the thumbnail file of the photo but will upload the source file once I have it. Colors of business card should flow. I am interested in doing the translucent clear plastic cards as well. My company is called CloudRiver in one word and the contact details are below:

Dale Hollings
555-318-4720
www.CloudRiverTx.example
dhollings_47@mailbox.example
Updates

Too much red. I'd rather focus on the blue and put some silver or grey in there.

New Files uploaded. Like the designs so far and am looking forward to seeing more.

Looking for a whole new direction. Let's forget about the plastic card. Let's focus on the blue more than red. I still haven't seen something that really grabs me.

Industry/Entity Type

Plastic

```html
<!DOCTYPE html>
<html lang="en">
<head>
<meta charset="utf-8">
<title>CloudRiver Business Card</title>
<link rel="stylesheet" href="https://fonts.googleapis.com/css2?family=Open+Sans:ital,wght@0,400;0,600;0,700;1,400&display=swap">
<style>
  :root {
    --backdrop: #dcd8d3;
    --card: #eef0f1;
    --card-edge: #d3d7da;
    --brand-blue: #1a8cc0;
    --band-blue-light: #3aaed2;
    --band-blue-dark: #1b82b3;
    --band-red-light: #ef2a30;
    --band-red-dark: #c3121a;
    --text-light: #ffffff;
    --text-soft: #eaf6fb;
  }
  html, body {
    margin: 0;
    width: 1200px;
    height: 969px;
    overflow: hidden;
    background: var(--backdrop);
    font-family: "Open Sans", Arial, sans-serif;
  }
  .business-card {
    position: absolute;
    left: 100px;
    top: 205px;
    width: 1000px;
    height: 559px;
    background: var(--card);
    border: 1px solid var(--card-edge);
    border-radius: 6px;
    overflow: hidden;
    box-shadow: 0 18px 40px rgba(0,0,0,0.12);
  }
  .card-bands {
    position: absolute;
    inset: 0;
  }
  .brand-name {
    position: absolute;
    left: 93px;
    top: 70px;
    margin: 0;
    font-size: 94px;
    font-weight: 600;
    letter-spacing: -2px;
    color: var(--brand-blue);
    line-height: 1;
  }
  .person-name {
    position: absolute;
    left: 91px;
    top: 325px;
    margin: 0;
    font-size: 44px;
    font-style: italic;
    font-weight: 400;
    color: var(--text-light);
    line-height: 1.2;
  }
  .contact-list {
    position: absolute;
    left: 96px;
    top: 398px;
    margin: 0;
    padding: 0;
    list-style: none;
  }
  .contact-item {
    display: flex;
    align-items: center;
    height: 33px;
    font-size: 23px;
    color: var(--text-soft);
  }
  .contact-icon {
    width: 20px;
    height: 20px;
    margin-right: 14px;
    flex: none;
  }
  .website {
    position: absolute;
    right: 36px;
    top: 429px;
    margin: 0;
    font-size: 21px;
    font-weight: 700;
    color: var(--text-light);
    line-height: 1.3;
    text-align: right;
    white-space: nowrap;
  }
</style>
</head>
<body>
  <div class="business-card">
    <svg class="card-bands" width="1000" height="559" viewBox="0 0 1000 559" aria-hidden="true">
      <defs>
        <linearGradient id="blue-band-fill" x1="0" y1="0" x2="1" y2="1">
          <stop offset="0" stop-color="var(--band-blue-light)"/>
          <stop offset="1" stop-color="var(--band-blue-dark)"/>
        </linearGradient>
        <linearGradient id="red-band-fill" x1="0" y1="0" x2="1" y2="1">
          <stop offset="0" stop-color="var(--band-red-light)"/>
          <stop offset="1" stop-color="var(--band-red-dark)"/>
        </linearGradient>
      </defs>
      <polygon class="blue-band" points="0,275 654,275 599,532 0,532" fill="url(#blue-band-fill)"/>
      <polygon class="red-band" points="640,403 1000,403 1000,559 607,559" fill="url(#red-band-fill)"/>
    </svg>

    <h1 class="brand-name">CloudRiver</h1>

    <h2 class="person-name">Dale Hollings</h2>

    <ul class="contact-list">
      <li class="contact-item">
        <svg class="contact-icon" viewBox="0 0 24 24" aria-hidden="true">
          <path fill="currentColor" d="M6.6 10.8a15.1 15.1 0 0 0 6.6 6.6l2.2-2.2a1 1 0 0 1 1-.25 11.4 11.4 0 0 0 3.6.57 1 1 0 0 1 1 1V20a1 1 0 0 1-1 1A17 17 0 0 1 3 4a1 1 0 0 1 1-1h3.5a1 1 0 0 1 1 1c0 1.250.2 2.450.57 3.57a1 1 0 0 1-.25 1z"/>
        </svg>
        <span class="contact-phone">555-318-4720</span>
      </li>
      <li class="contact-item">
        <svg class="contact-icon" viewBox="0 0 24 24" aria-hidden="true">
          <path fill="currentColor" d="M3 5h18a1 1 0 0 1 1 1v12a1 1 0 0 1-1 1H3a1 1 0 0 1-1-1V6a1 1 0 0 1 1-1zm1 2.2V17h16V7.2l-8 5.3z"/>
          <path fill="currentColor" d="M4 7h16l-8 5.2z" opacity="0.6"/>
        </svg>
        <span class="contact-email">dhollings_47@mailbox.example</span>
      </li>
    </ul>

    <p class="website">www.CloudRiverTx.example</p>
  </div>
</body>
</html>
```